New to ArtHarbor? This contest is for you!

Are you new to ArtHarbor and looking to enter your first contest? Look no further!

We're launching this special contest to help you get started on building a design portfolio at ArtHarbor!

Requirements:
Create a mini one-page portfolio featuring selection of 3-5 designs from your personal portfolio to sell yourself as a designer.

The submission (1 page portfolio) should showcase your design skills to our design quality team and to our designers.

We've mocked up a few layouts to provide a guide for how to layout your submission. Please see the attachments to the brief. (This is a guide only.)

The mini portfolio should grab attention and communicate who your personal design brand.

Designers are limited to 1 design submission, so show us your best work!

You must upload your entry before 12:00am 1 Oct 2016 UTC

This must be your very FIRST entry on ArtHarbor to be eligible to receive a prize. If you've already entered other ArtHarbor contests you won't be eligible to win the prizes.

Your design must adhere to our quality standards and be approved by our quality team to be eligible to receive a prize.

Target Market(s)

ArtHarbor quality team
ArtHarbor customers

Industry/Entity Type

Graphic Design

Requirements
Must have
• Showcase 3-5 of your best designs from your personal work on 1 page.
• The portfolio should grab our judges attention and communicate who you are as a designer.
Nice to have
• Text or descriptions about the work is optional
Should not have
• No individual design examples should be submitted.

```html
<!DOCTYPE html>
<html lang="en">
<head>
<meta charset="utf-8">
<title>Arin Kavade — Portfolio</title>
<link href="https://fonts.googleapis.com/css2?family=Roboto:wght@400;500;700&family=Open+Sans:wght@400;600&display=swap" rel="stylesheet">
<style>
:root{
  --pink:#d4185a;
  --pink-dark:#a5123f;
  --ink:#0b0b0b;
  --paper:#ffffff;
  --mist:#f0f0f0;
  --text:#1a1a1a;
  --green:#5cb531;
  --wine:#2c0b15;
  --field:#555555;
}
*{box-sizing:border-box;margin:0;padding:0}
html,body{width:1200px;height:1200px;overflow:hidden;background:var(--paper)}
body{position:relative;font-family:'Roboto',sans-serif;color:var(--text)}
.abs{position:absolute}

/* header */
.site-header{left:0;top:0;width:1200px;height:80px;background:var(--ink)}
.brand{left:44px;top:30px;color:#fff;font-size:25px;font-weight:500;padding-bottom:4px;border-bottom:2px solid var(--pink)}
.nav{right:258px;top:44px;display:flex;gap:28px}
.nav a{color:#fff;text-decoration:none;font-size:18px;letter-spacing:.3px;padding-bottom:2px}
.nav a.active{border-bottom:2px solid var(--pink)}

/* about */
.about{left:0;top:80px;width:1200px;height:272px;background:var(--paper)}
.portrait{left:84px;top:22px;width:224px;height:224px;border-radius:50%;background:radial-gradient(circle at 45% 40%,#c9d6e4,#7c97b5 55%,#2c4d78)}
.intro{left:360px;top:26px;width:740px}
.intro h1{font-size:23px;font-weight:400;margin-bottom:10px}
.intro p{font-size:21px;line-height:32px;margin-bottom:10px}
.hl{color:var(--pink)}

/* work */
.work{left:0;top:352px;width:1200px;height:438px;background:var(--pink)}
.arrow{width:64px;height:64px;border-radius:50%;background:var(--pink-dark)}
.arrow svg{width:64px;height:64px}
.card{overflow:hidden}
.card-app{left:89px;top:37px;width:241px;height:358px;background:var(--wine)}
.app-bar{left:0;top:0;width:241px;height:40px;background:#fff}
.app-title{left:0;top:11px;width:241px;text-align:center;color:var(--green);font-weight:700;font-size:14px;letter-spacing:.5px}
.album{left:45px;top:65px;width:154px;height:166px;background:#5a3d12}
.song{left:0;top:243px;width:241px;text-align:center;color:#eee;font-size:8px;line-height:11px}
.song i{font-size:6px;color:#bbb}
.time{top:290px;color:#eee;font-size:9px}
.progress{left:0;top:305px;width:241px;height:2px;background:#555}
.progress span{display:block;width:66px;height:2px;background:var(--green)}
.controls{left:0;top:307px;width:241px;height:51px;background:#f2f2f2}
.card-mark{left:360px;top:41px;width:222px;height:357px;background:#000;color:#fff}
.mark-name{left:0;top:160px;width:222px;text-align:center;font-size:27px;font-weight:700;letter-spacing:1px}
.mark-sub{left:0;top:196px;width:222px;text-align:center;font-size:7px;letter-spacing:.4px}
.card-greeting{left:610px;top:41px;width:227px;height:358px;background:linear-gradient(180deg,#5fc3ab,#58b9a0)}
.card-id{left:870px;top:41px;width:228px;height:358px;background:linear-gradient(150deg,#0a8fd9,#0bb2ec 55%,#5cc6ef)}
.id-name{left:0;top:140px;width:228px;text-align:center;color:#fff;font-size:48px;font-weight:700}

/* skills */
.skills{left:0;top:790px;width:1200px;height:192px;background:var(--mist);font-family:'Open Sans',sans-serif}
.skill{display:flex;align-items:center;gap:8px}
.skill-label{font-size:21px;text-align:right}
.bar{width:252px;height:18px;background:var(--ink)}
.bar span{display:block;height:18px;background:var(--pink)}

/* footer */
.site-footer{left:0;top:982px;width:1200px;height:218px;background:#000}
.social{top:48px;color:#fff;font-size:16px;font-weight:500;display:flex;align-items:center;gap:6px;transform:translateX(-50%)}
.social i{width:8px;height:8px;border-radius:50%;background:var(--pink)}
.email{left:403px;top:119px;width:272px;height:53px;border-radius:27px;background:var(--field);color:#777;font-family:'Open Sans',sans-serif;font-size:16px;display:flex;align-items:center;justify-content:center}
.cta{left:702px;top:119px;width:152px;height:53px;border-radius:27px;background:var(--pink);color:#fff;font-family:'Open Sans',sans-serif;font-size:12px;display:flex;align-items:center;justify-content:center}
</style>
</head>
<body>

<header class="site-header abs">
  <div class="brand abs">Arin Kavade</div>
  <nav class="nav abs">
    <a class="active" href="#about">ABOUT</a>
    <a href="#skills">SKILLS</a>
    <a href="#contact">GET IN TOUCH</a>
  </nav>
</header>

<section class="about abs" id="about">
  <div class="portrait abs" role="img" aria-label="Portrait photo of the designer in blue duotone"></div>
  <div class="intro abs">
    <h1>Hello, my name is <span class="hl">Arin</span></h1>
    <p>I’m freelancer <span class="hl">Web</span> and <span class="hl">Graphics</span> Designer. I love to work with inspring and <span class="hl">creative</span> agencies and people.</p>
    <p>I’m adaptable, ambitious, self-motivated, confident and down to earth individual combined with a limitless <span class="hl">imgination</span> and <span class="hl">creative</span> drive.</p>
  </div>
</section>

<section class="work abs">
  <div class="arrow abs" style="left:12px;top:200px">
    <svg viewBox="0 0 64 64"><polyline points="22,16 44,32 22,48" fill="none" stroke="#fff" stroke-width="8" stroke-linecap="round" stroke-linejoin="round"/></svg>
  </div>

  <div class="card card-app abs">
    <div class="app-bar abs">
      <svg class="abs" style="left:14px;top:14px" width="16" height="12"><rect y="0" width="16" height="2" fill="#5cb531"/><rect y="5" width="16" height="2" fill="#5cb531"/><rect y="10" width="16" height="2" fill="#5cb531"/></svg>
      <div class="app-title abs">TUNEDECK</div>
      <svg class="abs" style="left:226px;top:13px" width="4" height="14"><circle cx="2" cy="2" r="1.4" fill="#555"/><circle cx="2" cy="7" r="1.4" fill="#555"/><circle cx="2" cy="12" r="1.4" fill="#555"/></svg>
    </div>
    <div class="album abs"></div>
    <div class="song abs">Night Drive - Mira Lane ft. Jo Vale<br><i>Mira Lane ft. Jo Vale</i></div>
    <svg class="abs" style="left:110px;top:270px" width="22" height="8"><rect width="22" height="2" fill="#777"/><rect y="4" width="22" height="2" fill="#777"/></svg>
    <div class="time abs" style="left:7px">1:38</div>
    <div class="time abs" style="right:9px">4:53</div>
    <div class="progress abs"><span></span></div>
    <div class="controls abs">
      <svg width="241" height="51">
        <path d="M50 21 l5 0 l6 8 l5 0 M50 29 l5 0 l6 -8 l5 0" fill="none" stroke="#444" stroke-width="1.2"/>
        <polygon points="104,25 110,20 110,30" fill="#5cb531"/><polygon points="98,25 104,20 104,30" fill="#5cb531"/>
        <rect x="115" y="19" width="4" height="12" fill="#5cb531"/><rect x="122" y="19" width="4" height="12" fill="#5cb531"/>
        <polygon points="137,25 131,20 131,30" fill="#5cb531"/><polygon points="143,25 137,20 137,30" fill="#5cb531"/>
        <rect x="175" y="21" width="12" height="8" fill="none" stroke="#444" stroke-width="1.2"/>
      </svg>
    </div>
  </div>

  <div class="card card-mark abs">
    <div class="mark-name abs">KALPANTA</div>
    <div class="mark-sub abs">TRADING &amp; INFRASTRUCTURE PVT. LTD.</div>
  </div>

  <div class="card card-greeting abs" role="img" aria-label="Greeting card illustration with script title, a small bird on a blossoming branch and hearts"></div>

  <div class="card card-id abs">
    <div class="id-name abs">ARIN</div>
  </div>

  <div class="arrow abs" style="left:1114px;top:190px">
    <svg viewBox="0 0 64 64"><polyline points="42,16 20,32 42,48" fill="none" stroke="#fff" stroke-width="8" stroke-linecap="round" stroke-linejoin="round"/></svg>
  </div>
</section>

<section class="skills abs" id="skills">
  <div class="skill abs" style="right:758px;top:50px"><span class="skill-label">HTML5</span><div class="bar"><span style="width:90%"></span></div></div>
  <div class="skill abs" style="right:758px;top:101px"><span class="skill-label">CSS3</span><div class="bar"><span style="width:85%"></span></div></div>
  <div class="skill abs" style="right:758px;top:152px"><span class="skill-label">JavaScript</span><div class="bar"><span style="width:70%"></span></div></div>
  <div class="skill abs" style="right:144px;top:41px"><span class="skill-label">Vec</span><div class="bar"><span style="width:90%"></span></div></div>
  <div class="skill abs" style="right:144px;top:91px"><span class="skill-label">Pix</span><div class="bar"><span style="width:70%"></span></div></div>
  <div class="skill abs" style="right:144px;top:143px"><span class="skill-label">Web</span><div class="bar"><span style="width:80%"></span></div></div>
</section>

<footer class="site-footer abs" id="contact">
  <div class="social abs" style="left:516px"><i></i>Chirper</div>
  <div class="social abs" style="left:631px"><i></i>Hoopla</div>
  <div class="social abs" style="left:741px"><i></i>Folio</div>
  <div class="email abs">email address</div>
  <div class="cta abs">GET IN TOUCH</div>
</footer>

</body>
</html>
```